Postcard Mail Out - Wendell

We are a real estate company. We need a post card to mail out to potential clients to try and sale their land. We will attached a couple of post cards that we like but we do not want to copy them completely. We do need to put the Fair Dwelling Access and the Homebroker logos with a disclosure saying not intended to solicit currently listed properties. The image below is what we had started working on. We would like to include something about farm land, timber, maybe a pond, something along those lines. The PDF Files attached are a flyer that was mailed out by another company that we do not want to copy completely. Attached also will be our company's Logo.

Requirements
Must have
• We do need to put the Fair Dwelling Access and the Homebroker logos with a disclosure saying not intended to solicit currently listed properties.<br/><br/>At Cal Moreno Summit Realty, we are blessed to have one of the very best Rural Land Specialists available. Wendell has years of experience promoting and selling rural land properties. Wendell has earned the trust of many landowners, as he is so PASSIONATE in all regards to rural land, farms and ranches. He has made a wide range of landowners very happy throughout his years in Real Estate. Call him today and show him your property, and he will provide you with a free analysis and strategy to maximize the return on your property.
Nice to have
• A picture of Wendell has been added to use on the back of the post card with his phone and number. It would be nice to have a east Texas scenery picture behind him instead of an office.<br/><br/>Please include front and back of post card in your submission.
Should not have
• Should not have Ferris Dunmore's information on the postcard. That post card was just to show what we was wanting. The agent we want listed is Wendell Pruitt and his phone number is (555)413-2086.

```html
<!DOCTYPE html>
<html lang="en">
<head>
<meta charset="utf-8">
<title>Cal Moreno Summit Realty – Land Postcard</title>
<link rel="stylesheet" href="https://fonts.googleapis.com/css2?family=Roboto+Slab:wght@500;800&family=Cormorant+Garamond:wght@600&family=Montserrat:wght@500;600;700&family=Open+Sans:wght@400;700&display=swap">
<style>
  :root{
    --canvas:#ffffff;
    --paper-light:#f1ebe2;
    --paper-mid:#ded2c1;
    --paper-dark:#c9b79f;
    --ink:#1e1b19;
    --white:#ffffff;
    --muted:#cfc7bd;
    --accent:#f4a469;
    --accent-text:#f0935a;
    --field:#7d8a5a;
    --sky:#b9c7cf;
  }
  *{box-sizing:border-box;margin:0;padding:0}
  html,body{width:1200px;height:1200px;overflow:hidden;background:var(--canvas)}
  .canvas{position:relative;width:1200px;height:1200px}
  .card{
    position:absolute;left:271px;width:657px;height:438px;overflow:hidden;
    background:radial-gradient(ellipse at 55% 40%,var(--paper-light) 0%,var(--paper-mid) 70%,var(--paper-dark) 100%);
    box-shadow:0 3px 8px rgba(0,0,0,.35);
  }
  .card--front{top:143px}
  .card--back{top:651px}

  /* ---------- front ---------- */
  .band{position:absolute;left:0;top:0;width:657px;height:438px}
  .hole{position:absolute;width:20px;height:20px;border-radius:50%}
  .hole--dark{background:var(--ink)}
  .hole--light{background:var(--white)}
  .brand{
    position:absolute;top:58px;left:0;width:100%;
    display:flex;justify-content:center;align-items:center;gap:10px;
    font-family:"Roboto Slab",serif;font-weight:500;font-size:22px;color:var(--ink);
  }
  .brand__mark{width:34px;height:34px;background:var(--ink)}
  .headline{
    position:absolute;top:134px;left:0;width:100%;text-align:center;
    font-family:"Roboto Slab",serif;font-weight:800;font-size:40px;letter-spacing:1px;color:var(--ink);
  }
  .photo{position:absolute;top:206px;width:174px;height:117px;box-shadow:0 2px 4px rgba(0,0,0,.3)}
  .photo--meadow{left:67px;background:linear-gradient(180deg,#9fb0b5 0%,#6b7553 35%,#a88f5a 100%)}
  .photo--timber{left:254px;background:linear-gradient(180deg,#fbfbfb 0%,#fbfbfb 35%,#2d3327 55%,#3b3f2c 100%)}
  .photo--pond{left:440px;background:linear-gradient(180deg,#9bb7da 0%,#6c8a6c 45%,#2f84a5 100%)}
  .tagline{
    position:absolute;top:362px;left:0;width:100%;text-align:center;
    font-family:"Cormorant Garamond",serif;font-weight:600;font-size:28px;color:var(--white);
  }
  .contact{
    position:absolute;display:flex;align-items:center;gap:24px;
    font-family:"Open Sans",sans-serif;color:var(--white);
  }
  .contact--front{top:403px;left:0;width:100%;justify-content:center}
  .contact__item{display:flex;align-items:center;gap:6px}
  .contact__web{font-size:15px}
  .contact__phone{font-size:18px;font-weight:700}
  .icon{width:18px;height:18px}

  /* ---------- back ---------- */
  .panel{position:absolute;left:0;top:0;width:657px;height:438px}
  .scenery{
    position:absolute;left:300px;top:250px;width:357px;height:188px;
    background:linear-gradient(180deg,rgba(185,199,207,0) 0%,var(--sky) 25%,var(--field) 55%,#8e8a7a 100%);
  }
  .offer{position:absolute;left:14px;top:44px;width:330px;color:var(--white)}
  .offer__title{
    font-family:"Roboto Slab",serif;font-weight:500;font-size:17px;line-height:1.25;
    letter-spacing:1px;color:var(--accent-text);
  }
  .offer__rule{width:128px;height:2px;background:var(--white);margin:5px 0 16px}
  .offer__text{font-family:"Montserrat",sans-serif;font-weight:500;font-size:11.5px;line-height:1.3;letter-spacing:.4px;padding-left:6px}
  .offer__subtitle{
    font-family:"Roboto Slab",serif;font-weight:500;font-size:14.5px;color:var(--accent-text);
    margin:20px 0 8px;
  }
  .offer__list{list-style:none;font-family:"Montserrat",sans-serif;font-weight:500;font-size:11.5px;line-height:1.3;letter-spacing:.3px}
  .offer__list li{padding-left:12px;text-indent:-9px}
  .offer__list li::before{content:"• "}
  .disclosure{
    position:absolute;left:16px;top:336px;width:300px;
    font-family:"Montserrat",sans-serif;font-weight:500;font-size:8px;letter-spacing:.3px;color:var(--muted);
  }
  .contact--back{top:393px;left:8px;color:var(--ink)}
  .contact--back .contact__web{font-size:16px}
  .contact--back .contact__phone{font-size:19px}
  .stamp{position:absolute;left:554px;top:17px;width:78px;height:88px;border:2px solid var(--ink)}
  .indicia{
    position:absolute;left:460px;top:34px;width:82px;text-align:center;
    font-family:"Montserrat",sans-serif;font-weight:700;font-size:9.5px;line-height:1.25;color:var(--ink);
  }
  .address-line{position:absolute;left:394px;width:244px;height:2px;background:var(--ink)}
  .badge{
    position:absolute;top:274px;display:flex;flex-direction:column;align-items:center;gap:4px;
    font-family:"Montserrat",sans-serif;font-weight:700;font-size:8px;line-height:1.05;color:var(--ink);text-align:center;
  }
  .badge__mark{width:48px;height:48px;background:var(--ink)}
  .badge--fair{left:370px;width:74px}
  .badge--broker{left:456px;width:66px}
  .agent-photo{
    position:absolute;left:532px;top:274px;width:125px;height:164px;
    background:linear-gradient(180deg,#c9b8a4 0%,#b59f88 40%,#f4f4f2 58%,#e9e9e6 100%);
  }
  .agent-name{
    position:absolute;left:532px;top:418px;width:125px;text-align:center;
    font-family:"Montserrat",sans-serif;font-weight:700;font-size:10.5px;color:var(--ink);
  }
</style>
</head>
<body>
<main class="canvas">

  <!-- front of postcard -->
  <section class="card card--front" aria-label="Postcard front">
    <svg class="band" viewBox="0 0 657 438" aria-hidden="true">
      <path d="M0,318 Q330,262 657,300 L657,438 L0,438 Z" fill="var(--ink)"/>
    </svg>

    <span class="hole hole--dark" style="left:32px;top:30px"></span>
    <span class="hole hole--dark" style="left:605px;top:30px"></span>
    <span class="hole hole--light" style="left:32px;top:367px"></span>
    <span class="hole hole--light" style="left:605px;top:367px"></span>

    <div class="brand"><span class="brand__mark"></span>Cal Moreno Summit Realty</div>

    <h1 class="headline">LAND FOR SALE ?</h1>

    <div class="photo photo--meadow" role="img" aria-label="Rolling rural meadow with farmhouses and forest"></div>
    <div class="photo photo--timber" role="img" aria-label="Stand of dark timber behind an open field"></div>
    <div class="photo photo--pond" role="img" aria-label="Pond reflecting trees and a lakeside home"></div>

    <p class="tagline">Specializing In Rural Land Sales</p>

    <div class="contact contact--front">
      <span class="contact__item contact__web">
        <svg class="icon" viewBox="0 0 24 24" fill="none" stroke="currentColor" stroke-width="1.6"><circle cx="12" cy="12" r="10"/><ellipse cx="12" cy="12" rx="4.5" ry="10"/><path d="M2 12h20M4 6.5h16M4 17.5h16"/></svg>
        1summitprop.com
      </span>
      <span class="contact__item contact__phone">
        <svg class="icon" viewBox="0 0 24 24" fill="currentColor"><path d="M6.6 10.8a15.1 15.1 0 0 0 6.6 6.6l2.2-2.2a1 1 0 0 1 1-.25 11.4 11.4 0 0 0 3.6.57 1 1 0 0 1 1 1V20a1 1 0 0 1-1 1A17 17 0 0 1 3 4a1 1 0 0 1 1-1h3.5a1 1 0 0 1 1 1c0 1.25.2 2.45.57 3.57a1 1 0 0 1-.25 1z"/></svg>
        555-413-2086
      </span>
    </div>
  </section>

  <!-- back of postcard -->
  <section class="card card--back" aria-label="Postcard back">
    <div class="scenery" role="img" aria-label="East Texas countryside road and pasture"></div>

    <svg class="panel" viewBox="0 0 657 438" aria-hidden="true">
      <path d="M0,0 H262 C350,50 392,230 336,362 L0,362 Z" fill="var(--ink)"/>
      <path d="M0,360 H392 L346,438 H0 Z" fill="var(--accent)"/>
    </svg>

    <div class="offer">
      <h2 class="offer__title">THINKING ABOUT SELLING<br>YOUR LAND?</h2>
      <div class="offer__rule"></div>
      <p class="offer__text">Summit Realty is here for your local<br>Antler Ridge Properties Land Specialist<br>in East Texas. I would love to talk with<br>you about why landowners trust me to<br>uniquely market and sell their property<br>quickly for the best price possible.</p>
      <h3 class="offer__subtitle">At CAL MORENO SUMMIT REALTY we:</h3>
      <ul class="offer__list">
        <li>Provide the highest level of trust, communication and service.</li>
        <li>Identify the recreational value on your land.</li>
        <li>Reach qualified buyers and investors across the nation.</li>
      </ul>
    </div>

    <p class="disclosure">Not intended to solicit currently listed properties.</p>

    <div class="contact contact--back">
      <span class="contact__item contact__web">
        <svg class="icon" viewBox="0 0 24 24" fill="none" stroke="currentColor" stroke-width="1.6"><circle cx="12" cy="12" r="10"/><ellipse cx="12" cy="12" rx="4.5" ry="10"/><path d="M2 12h20M4 6.5h16M4 17.5h16"/></svg>
        1summitprop.com
      </span>
      <span class="contact__item contact__phone">
        <svg class="icon" viewBox="0 0 24 24" fill="currentColor"><path d="M6.6 10.8a15.1 15.1 0 0 0 6.6 6.6l2.2-2.2a1 1 0 0 1 1-.25 11.4 11.4 0 0 0 3.6.57 1 1 0 0 1 1 1V20a1 1 0 0 1-1 1A17 17 0 0 1 3 4a1 1 0 0 1 1-1h3.5a1 1 0 0 1 1 1c0 1.25.2 2.45.57 3.57a1 1 0 0 1-.25 1z"/></svg>
        555-413-2086
      </span>
    </div>

    <p class="indicia">PRSRT STD<br>US POSTAL<br>PAID<br>DELIVER<br>PERMIT 4</p>
    <div class="stamp"></div>

    <span class="address-line" style="top:154px"></span>
    <span class="address-line" style="top:191px"></span>
    <span class="address-line" style="top:229px"></span>

    <div class="badge badge--fair"><span class="badge__mark"></span>FAIR DWELLING ACCESS</div>
    <div class="badge badge--broker"><span class="badge__mark"></span>HOMEBROKER</div>

    <div class="agent-photo" role="img" aria-label="Portrait of agent Wendell Pruitt in a white company shirt"></div>
    <p class="agent-name">Wendell Pruitt</p>
  </section>

</main>
</body>
</html>
```